Larkwell Cafe Business Card

We are a café in Sydney.
see website for details. http://www.larkwellcafe.com.au

want a single sided business card - no person's name on there.
This is to hand out to customers
use the attached logo

Business

Contact Information for Business Card

Larkwell Café
Upper Floor,
517-521 Pellow St
Sydney NSW 2000
T: 9418 3052
W: www.larkwellcafe.com.au
F: facebook.com/LarkwellCafeSydney

Catering Available
Phone for Lunchtime Bookings

```html
<!DOCTYPE html>
<html lang="en">
<head>
<meta charset="utf-8">
<title>Larkwell Cafe — Business Card</title>
<link href="https://fonts.googleapis.com/css2?family=Cormorant+SC:wght@500&family=EB+Garamond:wght@400&display=swap" rel="stylesheet">
<style>
  :root {
    --paper: #ffffff;
    --ink: #1a1a1a;
    --frame: #111111;
    --rule: #555555;
    --brand-red: #7a0b0b;
    --table-light: #e3e9e9;
    --table-mid: #a9b8b9;
    --table-dark: #5f7274;
  }
  html, body {
    margin: 0;
    padding: 0;
    width: 1200px;
    height: 800px;
    overflow: hidden;
    background: var(--paper);
  }
  .card {
    position: relative;
    width: 1200px;
    height: 800px;
    background: var(--paper);
  }
  .card-art {
    position: absolute;
    inset: 0;
  }
  .cafe-name {
    position: absolute;
    left: 0;
    width: 1180px;
    top: 196px;
    margin: 0;
    text-align: center;
    font-family: "Cormorant SC", "Cormorant Garamond", serif;
    font-weight: 500;
    font-size: 112px;
    line-height: 1;
    letter-spacing: 1px;
    color: var(--brand-red);
  }
  .contact-line {
    position: absolute;
    left: 0;
    width: 1180px;
    top: 316px;
    margin: 0;
    text-align: center;
    font-family: "EB Garamond", serif;
    font-size: 28px;
    line-height: 1;
    color: var(--ink);
    letter-spacing: 0.3px;
  }
  .footnote {
    position: absolute;
    right: 118px;
    top: 651px;
    margin: 0;
    font-family: "EB Garamond", serif;
    font-size: 18px;
    line-height: 1;
    color: var(--ink);
  }
</style>
</head>
<body>
<main class="card">
  <svg class="card-art" width="1200" height="800" viewBox="0 0 1200 800" xmlns="http://www.w3.org/2000/svg">
    <defs>
      <linearGradient id="tableTone" x1="0" y1="0" x2="0" y2="1">
        <stop offset="0" stop-color="#ffffff" stop-opacity="0"/>
        <stop offset="0.28" stop-color="var(--table-light)"/>
        <stop offset="0.6" stop-color="var(--table-mid)"/>
        <stop offset="1" stop-color="var(--table-dark)"/>
      </linearGradient>
    </defs>
    <rect class="table-scene" x="35" y="400" width="1110" height="330" fill="url(#tableTone)"
          role="img" aria-label="Monochrome photo of a café table with a coffee cup, saucer and stacked plates"/>
    <rect class="outer-frame" x="79" y="89" width="1020" height="596" fill="none" stroke="var(--frame)" stroke-width="5"/>
    <rect class="inner-frame" x="88" y="99" width="1002" height="577" fill="none" stroke="var(--rule)" stroke-width="1"/>
    <line class="title-rule" x1="165" y1="315" x2="1015" y2="315" stroke="var(--rule)" stroke-width="1.2"/>
  </svg>

  <h1 class="cafe-name">Larkwell Cafe</h1>
  <p class="contact-line">517-521 Pellow Street | 9418 3052 | www.larkwellcafe.com.au/</p>
  <p class="footnote">*catering available, phone for lunchtime bookings</p>
</main>
</body>
</html>
```